My Brightmere Interiors llc fliers project

A flyer that will be direct mailed to customers. feel free to play with wording this is what i have now. I wlil include every service i offer in must haves and feel free to run a footer stating all my services
" My background, I'm Corvin Altabresh, I was born Into this business, Its what I know. So if your tired of waiting for weeks before your kitchen gets completed, as happens with other companies. If your tired of dealing with unreliable contractors deal with me. I'm so confident in my work, here are the numbers to previous customer. Mrs.Pettigrew-555-218-4093. Mr.Kowalczyk 555-730-1856. They will tell you I can provide you that dream kitchen and countertop installed, within a week. Mention this flyer to receive an additional 10% discoun
BrightMere Interiors llc
5810 amber fern CT
Falls church VA,22042
555-964-2071
Caltabresh@mailnest.example"

Target Market(s)

high income household income looking to get interior work done,

Industry/Entity Type

Church

Font styles to use
Serif

Requirements
Must have
• granite and marble kitchen and bathroom fabrication and install
• any flooring, hardwood, marble, carpet, laminate, install
• Kitchen cabinet design and install
• Bathroom remodeling
Nice to have
• an easy to read flyer that will give customers the info to reach me and understand what they do, if I put to much then reduce it.

```html
<!DOCTYPE html>
<html lang="en">
<head>
<meta charset="utf-8">
<title>BrightMere Interiors LLC – Mailer Postcard</title>
<link rel="stylesheet" href="https://fonts.googleapis.com/css2?family=Sorts+Mill+Goudy:ital@0;1&family=Libre+Baskerville:ital,wght@0,400;1,400&display=swap">
<style>
  :root {
    --ink-dark: #0b0b0b;
    --panel-mid: #2a2a2a;
    --gold: #f0b431;
    --gold-deep: #8a6a2c;
    --gold-light: #b8944e;
    --cream: #f3e7c4;
    --white: #ffffff;
    --rule: #dcdcdc;
    --stamp: #cfcfcf;
    --address: #222222;
  }
  * { margin: 0; padding: 0; box-sizing: border-box; }
  html, body { width: 1200px; height: 930px; overflow: hidden; background: var(--white); }
  .postcard { position: relative; width: 1200px; height: 930px; font-family: "Sorts Mill Goudy", serif; }

  .front {
    position: absolute; left: 0; top: 0; width: 580px; height: 767px;
    background: radial-gradient(ellipse 70% 45% at 50% 28%, var(--panel-mid) 0%, #151515 60%, var(--ink-dark) 100%);
    color: var(--white);
  }
  .services-title {
    position: absolute; left: 40px; top: 18px;
    font-family: "Libre Baskerville", serif; font-style: italic; font-size: 44px; font-weight: 400;
    color: var(--white); letter-spacing: 0.5px;
  }
  .services-title .accent { color: var(--gold); }

  .service-list { position: absolute; left: 36px; top: 82px; width: 520px; list-style: none; }
  .service-list li {
    position: relative; padding-left: 20px; font-size: 25px; line-height: 25px; margin-bottom: 12px;
  }
  .service-list li::before {
    content: ""; position: absolute; left: 0; top: 9px; width: 9px; height: 9px; border-radius: 50%;
    background: var(--gold);
  }

  .gallery { position: absolute; top: 296px; left: 27px; height: 140px; }
  .gallery-photo {
    position: absolute; top: 0; height: 140px; border: 2px solid #d8d8d8;
    box-shadow: 0 0 10px rgba(255,255,255,0.35);
  }
  .photo-kitchen-wide { left: 0; width: 213px; background: linear-gradient(160deg, #e9d3a8, #b07a3c 55%, #6b4a24); }
  .photo-kitchen-narrow { left: 218px; width: 78px; background: linear-gradient(170deg, #d9c7a4, #9b6a34 60%, #4d3a26); }
  .photo-kitchen-island { left: 302px; width: 208px; background: linear-gradient(165deg, #5a3a1e, #8c5a2c 50%, #2a1a10); }

  .refer-line {
    position: absolute; left: 0; width: 580px; top: 442px; text-align: center; font-size: 29px;
  }
  .refer-line em { font-family: "Libre Baskerville", serif; color: var(--gold); font-size: 27px; }

  .reference { position: absolute; font-size: 30px; }
  .reference .name { font-family: "Libre Baskerville", serif; font-style: italic; color: var(--gold); font-size: 27px; }
  .ref-one { left: 118px; top: 487px; }
  .ref-two { left: 108px; top: 519px; }

  .values-band {
    position: absolute; left: 0; top: 580px; width: 580px; height: 40px;
    background: linear-gradient(90deg, var(--gold-deep), var(--gold-light) 50%, var(--gold-deep));
    color: var(--cream); font-size: 30px; line-height: 40px; text-align: center; letter-spacing: 1.5px;
  }

  .brand-name {
    position: absolute; left: 40px; top: 660px; font-size: 38px; color: var(--white); line-height: 1;
  }
  .offer-note { position: absolute; right: 18px; top: 726px; font-size: 18px; }

  .mailing-address {
    position: absolute; left: 595px; width: 300px; top: 126px; text-align: center;
    font-family: "Libre Baskerville", serif; font-size: 18px; line-height: 21px; color: var(--address);
  }
  .stamp-box {
    position: absolute; left: 907px; top: 30px; width: 265px; height: 265px;
    border: 3px solid var(--stamp); background: var(--white);
  }
  .address-lines { position: absolute; left: 645px; top: 415px; }
</style>
</head>
<body>
<div class="postcard">
  <section class="front">
    <h1 class="services-title"><span class="accent">Services</span> we provide:</h1>
    <ul class="service-list">
      <li>Granite and marble kitchen and bathroom fabrication and install</li>
      <li>Any flooring, hardwood, marble, carpet, laminate, install</li>
      <li>Kitchen cabinet design and install</li>
      <li>Bathroom remodeling</li>
    </ul>

    <div class="gallery">
      <div class="gallery-photo photo-kitchen-wide" role="img" aria-label="Photo of a finished kitchen with oak cabinets and stainless appliances"></div>
      <div class="gallery-photo photo-kitchen-narrow" role="img" aria-label="Photo of a kitchen corner with range and cabinets"></div>
      <div class="gallery-photo photo-kitchen-island" role="img" aria-label="Photo of a dark wood kitchen with island and pendant lights"></div>
    </div>

    <p class="refer-line">Please refer to <em>previous customer.</em></p>
    <p class="reference ref-one"><span class="name">Mrs.Pettigrew</span> 555-218-4093</p>
    <p class="reference ref-two"><span class="name">Mr.Kowalczyk</span> 555-730-1856</p>

    <div class="values-band">PROUD • EXPERIENCED • HONEST</div>

    <p class="brand-name">BrightMere Interiors LLC</p>
    <p class="offer-note">*with this postcard</p>
  </section>

  <section class="back">
    <address class="mailing-address" style="font-style:normal">
      5810 Amber Fern CT<br>Falls Church<br>VA,22042
    </address>
    <div class="stamp-box"></div>
    <svg class="address-lines" width="500" height="260" viewBox="0 0 500 260" aria-hidden="true">
      <g stroke="#dcdcdc" stroke-width="3">
        <line x1="0" y1="5" x2="495" y2="5"/>
        <line x1="0" y1="89" x2="495" y2="89"/>
        <line x1="0" y1="170" x2="495" y2="170"/>
        <line x1="0" y1="253" x2="495" y2="253"/>
      </g>
    </svg>
  </section>
</div>
</body>
</html>
```